Cover für Podcast gesucht
Zielgruppe
Wir wollen einen PODCAST Rund um das Thema Business, Digitale Transformation und Tech starten. Unsere Zielgruppe sind Entscheidungsträger*innen die sich über aktuelle Trends, digitale und tech-orientierte Geschäftsmodelle sowie Tools und Management-Methoden auf dem Laufenden halten möchten.
Aufgabenstellung
ACHTUNG: ES HANDELT SICH HIERBEI UM EIN PODCAST COVER: Wir möchten auf dem Cover unsere beiden Fotos, die wir liefern, integriert haben sowie auch einen Schriftzug mit dem Namen 'wolkig verzweigt', der auch künftig als Logo für unsere Website fungieren soll. Das Cover soll das Thema 'digitalisierung', 'innovation', 'technologie / tech' 'trendy' umreißen.
Auf dem Cover sollten die beiden Bilder unserer Personen, der Schriftzug 'wolkig verzweigt' und darunter (subline) Business & Tech Talk stehen.

```html
<!DOCTYPE html>
<html lang="de">
<head>
<meta charset="utf-8">
<title>Wolkig Verzweigt – Podcast Cover</title>
<link rel="stylesheet" href="https://fonts.googleapis.com/css2?family=Montserrat:wght@300;400;600;800&display=swap">
<style>
  :root {
    --navy-deep: #1c2a42;
    --navy: #1d3457;
    --teal: #1f5866;
    --teal-light: #2f6b78;
    --accent-blue: #1aa3dc;
    --white: #ffffff;
    --photo-a: #5b7394;
    --photo-b: #2c3b55;
  }
  html, body {
    margin: 0;
    padding: 0;
    width: 1200px;
    height: 1200px;
    overflow: hidden;
    background: var(--navy-deep);
  }
  .cover {
    position: relative;
    width: 1200px;
    height: 1200px;
    overflow: hidden;
    font-family: "Montserrat", sans-serif;
    color: var(--white);
    background: linear-gradient(160deg, var(--navy-deep) 0%, var(--navy) 70%, #1c3861 100%);
  }
  .backdrop {
    position: absolute;
    inset: 0;
  }
  .brand-mark {
    position: absolute;
    top: 190px;
    left: 0;
    width: 1200px;
    display: flex;
    justify-content: center;
    align-items: center;
    gap: 18px;
  }
  .brand-mark__dot {
    width: 38px;
    height: 38px;
    border: 6px solid var(--white);
    border-radius: 50%;
    box-sizing: border-box;
  }
  .brand-mark__name {
    font-weight: 600;
    font-size: 32px;
    letter-spacing: 1px;
    text-transform: lowercase;
  }
  .title {
    position: absolute;
    left: 0;
    width: 1200px;
    text-align: center;
    margin: 0;
    line-height: 1;
  }
  .title--main {
    top: 380px;
    font-weight: 800;
    font-size: 132px;
    letter-spacing: 2px;
  }
  .title--sub {
    top: 532px;
    font-weight: 300;
    font-size: 84px;
    letter-spacing: 6px;
  }
  .subline {
    position: absolute;
    top: 636px;
    left: 0;
    width: 1200px;
    margin: 0;
    text-align: center;
    font-weight: 600;
    font-size: 30px;
    line-height: 1;
    letter-spacing: 4px;
    text-transform: uppercase;
    color: var(--accent-blue);
  }
  .host-photo {
    position: absolute;
    width: 360px;
    height: 360px;
    border-radius: 50%;
    border: 12px solid var(--white);
    box-sizing: border-box;
    background: radial-gradient(circle at 50% 35%, var(--photo-a) 0%, var(--photo-b) 80%);
  }
  .host-photo--left { left: 110px; top: 755px; }
  .host-photo--right { left: 741px; top: 755px; }
  .connectors {
    position: absolute;
    inset: 0;
  }
  .host-name {
    position: absolute;
    left: 482px;
    margin: 0;
    font-weight: 800;
    font-size: 48px;
    line-height: 1.05;
    letter-spacing: 1px;
    text-transform: uppercase;
  }
  .host-name--first { top: 722px; }
  .host-name--second { top: 985px; }
  .ampersand {
    position: absolute;
    left: 562px;
    top: 864px;
    width: 80px;
    text-align: center;
    font-weight: 800;
    font-size: 96px;
    line-height: 1;
  }
</style>
</head>
<body>
<main class="cover">
  <svg class="backdrop" width="1200" height="1200" viewBox="0 0 1200 1200" aria-hidden="true">
    <defs>
      <linearGradient id="blob-upper" x1="0" y1="0" x2="1" y2="1">
        <stop offset="0" stop-color="#2e5a6a" stop-opacity="0.85"/>
        <stop offset="1" stop-color="#1d3457" stop-opacity="0"/>
      </linearGradient>
      <linearGradient id="blob-lower" x1="0" y1="0" x2="1" y2="1">
        <stop offset="0" stop-color="#3a5a70" stop-opacity="0.7"/>
        <stop offset="1" stop-color="#1d3457" stop-opacity="0"/>
      </linearGradient>
    </defs>
    <path d="M330 250 C 330 80, 560 -20, 760 0 C 930 20, 1100 120, 1200 200 L 1200 1000 C 1050 900, 900 800, 740 700 C 560 600, 330 450, 330 250 Z" fill="url(#blob-upper)"/>
    <path d="M0 405 C 120 380, 300 420, 470 470 C 700 540, 950 700, 1200 920 L 1200 1200 L 0 1200 Z" fill="url(#blob-lower)" opacity="0.6"/>
    <path d="M1200 380 C 1050 460, 930 600, 880 760 C 840 900, 900 1050, 1000 1200 L 1200 1200 Z" fill="#24607a" opacity="0.25"/>
  </svg>

  <div class="brand-mark">
    <span class="brand-mark__dot"></span>
    <span class="brand-mark__name">wolkig verzweigt</span>
  </div>

  <h1 class="title title--main">WOLKIG</h1>
  <p class="title title--sub">VERZWEIGT</p>
  <p class="subline">Business &amp; Tech Talk</p>

  <div class="host-photo host-photo--left" role="img" aria-label="Porträtfoto von Markus Lindner"></div>
  <div class="host-photo host-photo--right" role="img" aria-label="Porträtfoto von Henrik Seidel"></div>

  <svg class="connectors" width="1200" height="1200" viewBox="0 0 1200 1200" aria-hidden="true">
    <polyline points="426,880 460,836 727,836" fill="none" stroke="var(--accent-blue)" stroke-width="4"/>
    <polyline points="482,1107 749,1107 806,1033" fill="none" stroke="var(--accent-blue)" stroke-width="4"/>
  </svg>

  <p class="host-name host-name--first">Markus<br>Lindner</p>
  <div class="ampersand">&amp;</div>
  <p class="host-name host-name--second">Henrik<br>Seidel</p>
</main>
</body>
</html>
```